Professional Engineering Web Design

Project Brief: Website Redesign for Mechanical Design Consultancy
Project Overview
I want to update and improve my current website to create a more professional, modern, and high-credibility online presence for my mechanical design consultancy.

Current site: https://valtrix.design/

The new website must communicate expertise, precision, and trust—matching the standard of top engineering and product design agencies.

Reference Websites (Style + Structure Inspiration)
These represent the quality, cleanliness, and professionalism I want to achieve:

https://plovenproductdesign.com/
https://www.quorvel.com/
https://dambrise-uk.com/
Brand Look
Professional, modern, engineering-focused aesthetic
Clean layouts and strong typography
High-quality imagery conveying precision, innovation, and mechanical expertise
Colour scheme and styling must follow my existing logo (attached in project)
Platform Requirements
The website must be built on WordPress
Should use a clean, flexible theme or modern page builder (Elementor, Gutenberg, Bricks, or similar)
Avoid overly complex custom coding so I can easily edit content later
Final deliverable must allow me to manage and update content without developer assistance
Functionality
Fast-loading, lightweight, and smooth user experience
Clean animations and transitions similar to the reference sites
Fully mobile responsive
Clear navigation and strong visual hierarchy
Contact forms optimised for lead generation
Optional: subtle scroll effects, case study sliders, icon animations, etc.
SEO Aspirations
Developer should recommend and implement a modern SEO strategy
Proper on-page SEO setup (titles, meta, schema, alt tags, heading structure)
Optimised site architecture for ranking and crawling
Aim: Generate leads through improved visibility and keyword targeting
Optional but useful: Google Analytics, Google Search Console setup
User Journeys
(Recommended structure)

The site should be crafted around clear, intuitive journeys for each type of visitor:

Potential new clients
Quickly understand what services I offer
View examples of past work / case studies
See credibility indicators (process, expertise, industries served)
Easily contact me or request a project discussion
Returning clients
Access updated portfolio items
Find contact details or book follow-up work easily
General visitors discovering through SEO
Be guided to core service areas
Understand my value proposition quickly
Be invited to learn more or make contact
The developer should design the structure to support these journeys smoothly.

Maintenance Expectations
Website will be maintained by me, so it should be easy to update using relatively basic WordPress skills
Use modular templates and simple backend structure
Avoid unnecessary plugins
Provide brief handover documentation if required
Hosting Preferences
Site is currently hosted via a family member
Open to discussing moving to a paid, reliable hosting provider if preferable for performance and maintainability
Developer may advise on the best hosting setup for WordPress
Content
Most content can be taken from the existing website
Developer is welcome to suggest improvements to structure, layout, and imagery
Must remain easy for me to edit or add new content later (e.g., new projects)
Deliverables
Fully built WordPress website
Clean, professional, modern design inspired by the reference sites
Mobile-responsive across all devices
SEO-ready structure and optimisations
Transfer of website and admin rights
Any design assets, templates, or documentation used

Coding

```html
<!DOCTYPE html>
<html lang="en">
<head>
<meta charset="utf-8">
<title>Valtrix Mechanical Design</title>
<link href="https://fonts.googleapis.com/css2?family=Noto+Sans:wght@400;500;600;700;800&family=Inter:wght@400;500;600&display=swap" rel="stylesheet">
<style>
:root{
  --blue:#3158ee;
  --blue-soft:#4a6cf4;
  --blue-deep:#2a3fb8;
  --blue-pale:#8fa6f8;
  --navy:#15183a;
  --ink:#111;
  --text:#333;
  --grey-label:#6b6b6b;
  --line:#3158ee;
  --white:#fff;
}
*{margin:0;padding:0;box-sizing:border-box}
html,body{width:1200px;height:3750px;overflow:hidden}
body{position:relative;background:var(--white);font-family:"Noto Sans",sans-serif;color:var(--text)}
.abs{position:absolute}
a{color:inherit;text-decoration:none}

/* top bar */
.topbar{left:0;top:0;width:1200px;height:38px;background:var(--blue);color:#fff;font-size:13px;font-weight:600}
.topbar .item{top:7px;display:flex;align-items:center;gap:9px}
.icon-dot{width:24px;height:24px;border-radius:50%;background:#fff;display:flex;align-items:center;justify-content:center}

/* header */
.header{left:0;top:38px;width:1200px;height:96px;background:#fff}
.brand{display:flex;align-items:center;gap:8px}
.brand-dot{width:30px;height:30px;border-radius:50%;background:var(--blue)}
.brand-name{font-weight:700;font-size:26px;color:var(--ink);letter-spacing:1px}
.nav{left:333px;top:36px;display:flex;gap:46px;font-size:14px;font-weight:500;color:var(--ink)}
.search{left:868px;top:23px;width:180px;height:48px;border-radius:24px;background:var(--blue-pale);display:flex;align-items:center;gap:16px;padding-left:6px;font-size:15px;font-weight:600;color:var(--navy)}
.search .ring{width:38px;height:38px;border-radius:50%;background:var(--blue);display:flex;align-items:center;justify-content:center}

/* hero */
.hero{left:0;top:134px;width:1200px;height:562px;overflow:hidden}
.hero-photo{left:0;top:0;width:1200px;height:562px;background:radial-gradient(circle at 70% 40%,#b86a2a 0,#4f4a44 18%,#22455f 45%,#163050 100%)}
.hero-panel{left:0;top:0}
.badge{left:150px;top:145px;height:28px;padding:0 12px 0 8px;border-radius:14px;background:var(--blue-soft);display:flex;align-items:center;gap:8px;color:#fff;font-size:12px;letter-spacing:2px;font-weight:500}
.badge i{width:14px;height:14px;border-radius:50%;background:#fff;display:block}
.hero h1{left:150px;top:186px;font-size:35px;line-height:42px;font-weight:700;color:#fff}
.hero p{left:150px;top:288px;width:440px;font-size:13.5px;line-height:22px;color:#fff}
.btn{display:flex;align-items:center;gap:10px;height:40px;padding:0 16px 0 9px;background:var(--blue);color:#fff;font-size:14px;font-weight:500;border-radius:3px}
.btn .ring{width:24px;height:24px;border-radius:50%;background:#fff;display:block}
.btn.plain{padding:0 17px}
.hero .btns{left:150px;top:366px;display:flex;gap:12px}

/* who */
.who-photo{left:150px;top:818px;width:498px;height:498px;border-radius:50%;background:radial-gradient(circle at 40% 40%,#8a96a8,#3d4451 70%,#2a2e36)}
.who h2{left:687px;top:888px;font-size:37px;font-weight:700;color:var(--ink)}
.who .lead{left:687px;top:942px;width:360px;font-size:14px;line-height:22px;font-weight:500;color:var(--ink)}
.who .body{left:687px;top:1030px;width:365px;font-size:13.5px;line-height:22.5px;color:var(--ink)}
.who .btn{left:687px;top:1191px}

/* expertise */
.sec-title{left:0;width:1200px;text-align:center;font-weight:700;color:var(--ink)}
.sec-sub{left:0;width:1200px;text-align:center;font-size:14px;color:var(--ink)}
.card{width:291px;height:248px;border:1.5px solid var(--line);border-radius:6px;padding:16px 22px}
.card .ico{width:66px;height:66px;border-radius:50%;border:1.5px solid var(--line);display:flex;align-items:center;justify-content:center}
.card h3{margin-top:22px;font-size:18px;font-weight:600;color:var(--ink)}
.card p{margin-top:14px;font-size:13px;line-height:22px;color:var(--text)}
.card .more{margin-top:16px;display:flex;align-items:center;gap:6px;font-size:13.5px;font-weight:600;color:var(--blue)}

/* work */
.work{left:0;top:1849px;width:1200px;height:657px;background:linear-gradient(135deg,#3a55d8,#2f4bc9 50%,#3b5be0)}
.work h2{top:60px;font-size:46px;color:#fff}
.work .sec-sub{top:98px;color:#fff}
.proj{width:288px;height:180px;border-radius:4px;overflow:hidden;background:#fff}
.proj .shot{height:128px;display:flex;align-items:center;justify-content:center}
.proj .shot span{width:140px;height:100px;border-radius:8px;display:block}
.proj .label{height:52px;background:var(--grey-label);color:#fff;font-size:14.5px;font-weight:600;display:flex;align-items:center;justify-content:center}
.work .btn{left:522px;top:572px;height:36px;background:var(--blue);box-shadow:0 0 0 1px rgba(255,255,255,.25)}

/* testimonials */
.testi{width:332px;height:214px;background:var(--blue-soft);border:2px solid var(--blue);border-radius:10px;color:#fff;text-align:center;padding-top:22px}
.testi .avatar{width:50px;height:50px;border-radius:50%;margin:0 auto;background:linear-gradient(#c99a78,#6a4a3a);border:2px solid #fff}
.testi .name{margin-top:8px;font-size:13.5px}
.testi .role{font-size:10.5px;opacity:.9;margin-top:2px}
.testi .quote{margin:10px auto 0;width:290px;font-size:13px;line-height:22px;opacity:.92}
.arrow{width:52px;height:52px;border-radius:50%;display:flex;align-items:center;justify-content:center}
.dots{left:575px;top:2962px;display:flex;gap:5px}
.dots i{width:7px;height:7px;border-radius:50%;background:var(--blue-soft);display:block}
.dots i.on{background:var(--navy)}

/* cta + footer */
.footer{left:0;top:3308px;width:1200px;height:442px;background:var(--navy)}
.cta{left:150px;top:3055px;width:898px;height:374px;border-radius:60px 60px 60px 0;overflow:hidden;background:linear-gradient(120deg,#dfe4ea,#aab3bf 60%,#6d7480)}
.cta h2{left:33px;top:108px;font-size:37px;line-height:47px;font-weight:700;color:#fff}
.cta p{left:35px;top:205px;font-size:13px;color:#fff}
.cta .btns{left:36px;top:233px;display:flex;gap:12px}
.cta .btn{height:38px}
.foot-brand{left:150px;top:3483px}
.foot-text{left:150px;top:3575px;width:340px;font-size:12px;line-height:19px;color:#b8bbd0;font-family:"Inter",sans-serif}
.foot-col{top:3536px;font-family:"Inter",sans-serif;font-size:12px;color:#b8bbd0}
.foot-col h4{color:#fff;font-size:12px;font-weight:600;margin-bottom:16px}
.foot-col li{list-style:none;margin-bottom:10px}
.foot-rule{left:150px;top:3686px;width:898px;height:1px;background:#2c3058}
.foot-base{top:3711px;font-family:"Inter",sans-serif;font-size:11px;color:#b8bbd0}
</style>
</head>
<body>

<div class="abs topbar">
  <div class="abs item" style="left:150px">
    <span class="icon-dot"><svg width="13" height="13" viewBox="0 0 24 24"><path fill="#3158ee" d="M6.6 10.8a15 15 0 0 0 6.6 6.6l2.2-2.2c.3-.3.7-.4 1-.2 1.1.4 2.3.6 3.6.6.6 0 1 .4 1 1V20c0 .6-.4 1-1 1A17 17 0 0 1 3 4c0-.6.4-1 1-1h3.5c.6 0 1 .4 1 1 0 1.3.2 2.5.6 3.6.1.3 0 .7-.2 1z"/></svg></span>
    <a href="mailto:info@valtrix.design">info@valtrix.design</a>
  </div>
  <div class="abs item" style="left:912px;font-size:12px">
    <span class="icon-dot"><svg width="13" height="13" viewBox="0 0 24 24"><path fill="#15183a" d="M3 5h18v14H3z"/><path d="M3 6l9 7 9-7" fill="none" stroke="#fff" stroke-width="2"/></svg></span>
    +44 (0) 7700 900418
  </div>
</div>

<header class="abs header">
  <div class="abs brand" style="left:150px;top:30px">
    <span class="brand-dot"></span><span class="brand-name">valtrix</span>
  </div>
  <nav class="abs nav"><a href="#">Home Page</a><a href="#">Portfolio</a><a href="#">Our Services</a><a href="#">Contact Us</a></nav>
  <div class="abs search"><span class="ring"><svg width="18" height="18" viewBox="0 0 24 24" fill="none" stroke="#fff" stroke-width="2.4"><circle cx="10" cy="10" r="6.5"/><path d="M15 15l5 5"/></svg></span>Search</div>
</header>

<section class="abs hero">
  <div class="abs hero-photo" role="img" aria-label="Glowing orange mechanical gears over a blue CAD blueprint background"></div>
  <svg class="abs hero-panel" width="620" height="562" viewBox="0 0 620 562">
    <path d="M0 0H430C540 0 604 110 604 250C604 430 500 562 340 562H0Z" fill="#2f56e6" fill-opacity=".9" stroke="#4a74ff" stroke-width="3"/>
  </svg>
  <div class="abs badge"><i></i>Engineering Excellence</div>
  <h1 class="abs">Mechanical CAD Design<br>Cutting Edge Engineering</h1>
  <p class="abs">UK-based mechanical design consultancy delivering end-to-end product development—from concept to full production.</p>
  <div class="abs btns"><a class="btn" href="#"><span class="ring"></span>Explore Our Services</a><a class="btn plain" href="#">View Our Work</a></div>
</section>

<section class="who">
  <svg class="abs" style="left:150px;top:818px" width="498" height="498">
    <defs><clipPath id="whoClip"><circle cx="249" cy="249" r="249"/></clipPath></defs>
  </svg>
  <div class="abs who-photo" role="img" aria-label="Engineer in glasses working at a computer in an office"></div>
  <h2 class="abs">Who We Are</h2>
  <p class="abs lead">Experienced Mechanical Engineers with 12+ years of industry work across automotive, medical, consumer &amp; industrial.</p>
  <p class="abs body">Daniel Hartwell is the Chief Engineer at Valtrix Mechanical Design. He has 11 years experience working as a mechanical design engineer in multiple industries including high performance automotive, consumer products, medical, industrial plus many more. He has worked in multiple roles across a wide range of products.</p>
  <a class="abs btn" href="#"><span class="ring"></span>Start Your Project</a>
</section>

<section class="expertise">
  <h2 class="abs sec-title" style="top:1372px;font-size:46px">Our Expertise</h2>
  <p class="abs sec-sub" style="top:1447px">High-Performance Mechanical Design for Real-World Products.</p>

  <div class="abs card" style="left:150px;top:1511px">
    <div class="ico"><svg width="34" height="34" viewBox="0 0 24 24" fill="none" stroke="#3158ee" stroke-width="1.4"><path d="M4 20L20 4M14 4l6 6M4 4l16 16"/></svg></div>
    <h3>Bespoke Product Design</h3>
    <p>Innovative design from concept through the full development life cycle.</p>
    <a class="more" href="#">Learn More <svg width="14" height="12" viewBox="0 0 14 12" fill="none" stroke="#3158ee" stroke-width="2"><path d="M0 6h12M7 1l5 5-5 5"/></svg></a>
  </div>
  <div class="abs card" style="left:454px;top:1511px">
    <div class="ico"><svg width="34" height="34" viewBox="0 0 24 24" fill="none" stroke="#3158ee" stroke-width="1.4"><path d="M3 5h18v11H3zM9 20h6M12 16v4"/><path d="M12 7l3 1.6v3.2L12 13.4 9 11.8V8.6z"/></svg></div>
    <h3>3D Modelling and Drawings</h3>
    <p>We create 3D CAD, 2D engineering drawings and photorealistic renders.</p>
    <a class="more" href="#">Learn More <svg width="14" height="12" viewBox="0 0 14 12" fill="none" stroke="#3158ee" stroke-width="2"><path d="M0 6h12M7 1l5 5-5 5"/></svg></a>
  </div>
  <div class="abs card" style="left:759px;top:1511px">
    <div class="ico"><svg width="34" height="34" viewBox="0 0 24 24" fill="none" stroke="#3158ee" stroke-width="1.4"><path d="M2 21V12l5-3v3l5-3v3l5-3V4h4v17z"/><path d="M5 17h2M9 17h2M13 17h2"/></svg></div>
    <h3>Design for Manufacture</h3>
    <p>Creating designs optimised for prototype and production manufacture.</p>
    <a class="more" href="#">Learn More <svg width="14" height="12" viewBox="0 0 14 12" fill="none" stroke="#3158ee" stroke-width="2"><path d="M0 6h12M7 1l5 5-5 5"/></svg></a>
  </div>
</section>

<section class="abs work">
  <h2 class="abs sec-title" style="top:38px;font-size:46px;color:#fff">Our Work</h2>
  <p class="abs sec-sub" style="top:98px;color:#fff">Showcasing Projects Across Industries</p>

  <div class="abs proj" style="left:150px;top:165px"><div class="shot" role="img" aria-label="Electrical switchgear cabinet render"><span style="background:linear-gradient(#8d949c,#4f575f)"></span></div><div class="label">Electrical Switchgear</div></div>
  <div class="abs proj" style="left:456px;top:165px"><div class="shot" role="img" aria-label="Three-piece alloy wheel render"><span style="width:110px;height:110px;border-radius:50%;background:radial-gradient(#f1f1f1,#9a9a9a 55%,#2c2c2c)"></span></div><div class="label">3-Piece Alloy Wheels</div></div>
  <div class="abs proj" style="left:762px;top:165px"><div class="shot" role="img" aria-label="Dual clutch transmission assembly render"><span style="background:linear-gradient(#4a4d52,#15171a)"></span></div><div class="label">Dual Clutch Transmission Design</div></div>
  <div class="abs proj" style="left:150px;top:360px"><div class="shot" role="img" aria-label="Go-kart simulator rig render"><span style="height:70px;background:linear-gradient(#c9cbc2,#4a4c4f)"></span></div><div class="label">Go-Kart Simulator Design</div></div>
  <div class="abs proj" style="left:456px;top:360px"><div class="shot" role="img" aria-label="Action camera mount render"><span style="width:170px;height:40px;background:linear-gradient(90deg,#2b2b2b,#c9a227)"></span></div><div class="label">Action camera mount</div></div>
  <div class="abs proj" style="left:762px;top:360px"><div class="shot" role="img" aria-label="Luxury fountain pen on a stand render"><span style="width:110px;height:80px;background:linear-gradient(135deg,#b8742e,#5a3716)"></span></div><div class="label">NORIV Luxury Pen</div></div>

  <a class="abs btn" href="#"><span class="ring"></span>View Case Study</a>
</section>

<section class="testimonials">
  <h2 class="abs sec-title" style="top:2588px;font-size:46px">Testimonials</h2>
  <p class="abs sec-sub" style="top:2650px">What Our Clients Say</p>

  <div class="abs arrow" style="left:21px;top:2794px;border:2px solid var(--blue)"><svg width="14" height="18" viewBox="0 0 14 18" fill="none" stroke="#3158ee" stroke-width="2.4"><path d="M10 2L3 9l7 7"/></svg></div>
  <div class="abs arrow" style="left:1126px;top:2794px;background:var(--blue)"><svg width="14" height="18" viewBox="0 0 14 18" fill="none" stroke="#fff" stroke-width="2.4"><path d="M4 2l7 7-7 7"/></svg></div>

  <div class="abs testi" style="left:90px;top:2713px"><div class="avatar" role="img" aria-label="Client portrait"></div><div class="name">Mara</div><div class="role">Manager</div><p class="quote">Lorem ipsum dolor sit amet, consectetur adipiscing elit, sed do eiusmod tempor incididunt ut labore et dolore magna aliqua. Quis ipsum</p></div>
  <div class="abs testi" style="left:434px;top:2713px"><div class="avatar" role="img" aria-label="Client portrait"></div><div class="name">Owen Calder</div><div class="role">Designer Engineer</div><p class="quote">Lorem ipsum dolor sit amet, consectetur adipiscing elit, sed do eiusmod tempor incididunt ut labore et dolore magna aliqua. Quis ipsum</p></div>
  <div class="abs testi" style="left:779px;top:2713px"><div class="avatar" role="img" aria-label="Client portrait"></div><div class="name">Lewis</div><div class="role">Manager</div><p class="quote">Lorem ipsum dolor sit amet, consectetur adipiscing elit, sed do eiusmod tempor incididunt ut labore et dolore magna aliqua. Quis ipsum</p></div>

  <div class="abs dots"><i></i><i></i><i class="on"></i><i></i><i></i></div>
</section>

<footer class="abs footer"></footer>

<section class="abs cta">
  <div class="abs" style="left:0;top:0;width:898px;height:374px" role="img" aria-label="Engineers working at computer workstations in a bright lab"></div>
  <svg class="abs" style="left:0;top:0" width="520" height="374" viewBox="0 0 520 374">
    <path d="M0 374V60Q0 0 60 0H300C430 0 512 90 512 190C512 300 430 374 320 374Z" fill="#3158ee" fill-opacity=".82" stroke="#4a74ff" stroke-width="3"/>
  </svg>
  <h2 class="abs">Ready to Start Your Next<br>Engineering Project?</h2>
  <p class="abs">Let's discuss your requirements and create a tailored solution.</p>
  <div class="abs btns"><a class="btn" href="#"><span class="ring"></span>Book a Consultation</a><a class="btn plain" href="#">Send an Enquiry</a></div>
</section>

<div class="abs brand foot-brand"><span class="brand-dot" style="width:44px;height:44px"></span><span class="brand-name" style="color:#fff;font-size:32px">valtrix</span></div>
<p class="abs foot-text">Precision mechanical design and engineering consultancy delivering innovative solutions for complex challenges.</p>
<div class="abs foot-col" style="left:611px"><h4>Quick Links</h4><ul><li>Services</li><li>Portfolio</li><li>About</li><li>Contact</li></ul></div>
<div class="abs foot-col" style="left:842px"><h4>Legal</h4><ul><li>Privacy Policy</li><li>Terms of Service</li></ul></div>
<div class="abs foot-rule"></div>
<div class="abs foot-base" style="left:150px">© 2024 Valtrix Design. All rights reserved.</div>
<div class="abs foot-base" style="left:911px">Built with precision and care</div>

</body>
</html>
```